Stationery for tax services company
Ledger Harbor Advisors
Stationery for tax services company - Financial Services
Creative Brief
Simple
Colin T. Westbrook, EA, JD, MST
President
4817 North Palomar Avenue, Suite 6 Honolulu, HI 96814
fileclearhelp@mailvora.net
www.LedgerHarborAdvisors.net
I also need business cards for the 2 following people: [Beth Colton, EA / Tax Preparer] [Marla Penhurst / Executive Assistant]
We need a design for business cards, letterhead page 1 of 2, letterhead page 2 of 2, envelopes small, label for large envelopes, fax cover sheet, email signature, and presentation folders.

```html
<!DOCTYPE html>
<html lang="en">
<head>
<meta charset="utf-8">
<title>Ledger Harbor Advisors Stationery</title>
<link rel="stylesheet" href="https://fonts.googleapis.com/css2?family=Cinzel:wght@600&family=Open+Sans:wght@400;600&display=swap">
<style>
  :root{
    --backdrop:#e4e5e8;
    --paper:#ffffff;
    --navy:#1b2070;
    --navy-deep:#10134a;
    --blue:#2f3c9e;
    --silver:#a9adb5;
    --silver-light:#d4d6db;
    --ink:#3a3d4a;
    --label:#6b6e78;
    --faint:#eef0f4;
  }
  *{box-sizing:border-box;margin:0;padding:0}
  html,body{width:1200px;height:444px;overflow:hidden;background:var(--backdrop)}
  body{position:relative;font-family:"Open Sans",Arial,sans-serif;color:var(--ink)}
  .item{position:absolute;box-shadow:0 2px 5px rgba(0,0,0,.25);overflow:hidden;background:var(--paper)}
  .label{position:absolute;font-size:5px;color:var(--label);text-align:center;white-space:nowrap}
  .brand{font-family:"Cinzel",Georgia,serif;font-weight:600;color:var(--navy);line-height:1.05;text-transform:uppercase;letter-spacing:.3px;white-space:nowrap}
  .brand-on-dark{color:#fff}
  .contact{font-size:3.6px;line-height:1.5;color:var(--ink);white-space:nowrap}
  .wave{position:absolute;left:0;bottom:0;width:100%;display:block}
  .faint-name{position:absolute;font-family:"Cinzel",Georgia,serif;font-weight:600;color:var(--faint);text-transform:uppercase;text-align:center;line-height:1}

  /* business cards */
  .card{left:26px;width:114px}
  .card-front{top:86px;height:128px}
  .card-front .contact{position:absolute;left:56px;top:10px}
  .card-front .brand{position:absolute;left:9px;top:54px;font-size:9px}
  .card-back{top:234px;height:58px;background:linear-gradient(160deg,var(--blue),var(--navy-deep))}
  .card-back .brand{position:absolute;left:0;right:0;top:19px;text-align:center;font-size:8px}
  .card-alt{top:320px;height:58px}
  .card-alt .brand{position:absolute;left:0;right:0;top:17px;text-align:center;font-size:7.5px}

  /* letterheads */
  .letterhead{top:19px;width:272px;height:384px}
  .lh-one{left:214px}
  .lh-two{left:506px}
  .letterhead .brand{position:absolute;left:16px;top:16px;font-size:9px}
  .letterhead .contact{position:absolute;left:160px;top:16px}
  .letterhead .faint-name{left:16px;right:16px;top:150px;font-size:24px}

  /* envelopes */
  .env{left:826px;width:300px;height:80px}
  .env-dark{top:40px;background:linear-gradient(160deg,var(--blue),var(--navy-deep))}
  .env-grey{top:130px;background:linear-gradient(180deg,#f3f4f6,#d9dbe0)}
  .env-plain{top:220px}
  .env-front{top:310px;height:92px}
  .env .flap{position:absolute;left:0;top:0;width:100%;height:100%;display:block}
  .env-front .brand{position:absolute;left:14px;top:12px;font-size:7px}
  .env-front .contact{position:absolute;left:14px;top:24px}
</style>
</head>
<body>

  <section class="item card card-front" aria-label="Business card front">
    <div class="contact">
      Colin T. Westbrook, EA<br>President<br>4817 North Palomar Avenue, Suite 6<br>Honolulu, HI 96814<br>Phone 808 555 0142<br>fileclearhelp@mailvora.net
    </div>
    <div class="brand">Ledger Harbor<br>Advisors</div>
    <svg class="wave" viewBox="0 0 114 22" height="22" preserveAspectRatio="none">
      <path d="M0 12 Q57 2 114 8 L114 22 L0 22Z" fill="var(--navy)"/>
      <path d="M0 10 Q57 0 114 6" stroke="var(--silver)" stroke-width="1.2" fill="none"/>
    </svg>
  </section>
  <div class="label" style="left:26px;top:217px;width:114px">Business Card Front</div>

  <section class="item card card-back" aria-label="Business card back">
    <div class="brand brand-on-dark">Ledger Harbor<br>Advisors</div>
  </section>
  <div class="label" style="left:26px;top:295px;width:114px">Business Card Back</div>

  <section class="item card card-alt" aria-label="Business card alternate">
    <div class="brand">Ledger Harbor<br>Advisors</div>
    <svg class="wave" viewBox="0 0 114 10" height="10" preserveAspectRatio="none">
      <path d="M0 6 Q57 0 114 4 L114 10 L0 10Z" fill="var(--navy)"/>
    </svg>
  </section>
  <div class="label" style="left:26px;top:381px;width:114px">Business Card Alt</div>

  <section class="item letterhead lh-one" aria-label="Letterhead page one">
    <div class="brand">Ledger Harbor<br>Advisors</div>
    <div class="contact">4817 North Palomar Avenue, Suite 6<br>Honolulu, HI 96814<br>fileclearhelp@mailvora.net<br>www.LedgerHarborAdvisors.net</div>
    <div class="faint-name">Ledger<br>Harbor<br>Advisors</div>
    <svg class="wave" viewBox="0 0 272 36" height="36" preserveAspectRatio="none">
      <path d="M0 24 Q136 6 272 16 L272 36 L0 36Z" fill="var(--navy)"/>
      <path d="M0 20 Q136 2 272 12" stroke="var(--silver)" stroke-width="2" fill="none"/>
    </svg>
  </section>
  <div class="label" style="left:214px;top:408px;width:272px">Letterhead Page 1</div>

  <section class="item letterhead lh-two" aria-label="Letterhead page two">
    <div class="brand">Ledger Harbor<br>Advisors</div>
    <div class="faint-name">Ledger<br>Harbor<br>Advisors</div>
    <svg class="wave" viewBox="0 0 272 36" height="36" preserveAspectRatio="none">
      <path d="M0 24 Q136 6 272 16 L272 36 L0 36Z" fill="var(--navy)"/>
      <path d="M0 20 Q136 2 272 12" stroke="var(--silver)" stroke-width="2" fill="none"/>
    </svg>
  </section>
  <div class="label" style="left:506px;top:408px;width:272px">Letterhead Page 2</div>

  <section class="item env env-dark" aria-label="Envelope back, dark">
    <svg class="flap" viewBox="0 0 300 80" preserveAspectRatio="none">
      <path d="M0 0 L150 42 L300 0Z" fill="rgba(0,0,0,.14)" stroke="rgba(255,255,255,.35)" stroke-width="0.8"/>
    </svg>
  </section>
  <div class="label" style="left:826px;top:30px;width:300px">Envelope Back</div>

  <section class="item env env-grey" aria-label="Envelope back, silver">
    <svg class="flap" viewBox="0 0 300 80" preserveAspectRatio="none">
      <path d="M0 0 L150 40 L300 0Z" fill="var(--silver)"/>
    </svg>
  </section>

  <section class="item env env-plain" aria-label="Envelope back, white">
    <svg class="flap" viewBox="0 0 300 80" preserveAspectRatio="none">
      <path d="M0 0 L150 40 L300 0" stroke="var(--silver-light)" stroke-width="1" fill="none"/>
    </svg>
  </section>

  <section class="item env env-front" aria-label="Envelope front">
    <div class="brand">Ledger Harbor Advisors</div>
    <div class="contact">4817 North Palomar Avenue, Suite 6<br>Honolulu, HI 96814</div>
    <svg class="wave" viewBox="0 0 300 14" height="14" preserveAspectRatio="none">
      <path d="M0 9 Q150 0 300 5 L300 14 L0 14Z" fill="var(--navy)"/>
    </svg>
  </section>
  <div class="label" style="left:826px;top:406px;width:300px">Envelope Front</div>

</body>
</html>
```